Business Card Design Project

We need a business card design for a consultancy called 'Maple Ridge'. The design should communicate innovation and professionalism. The colors used should complement our logo. Please include source files for winning design.
Updates

Industry/Entity Type

Business

Colors

Designer to choose colors to be used in the design.

Requirements
Must have
• Card size should be 85mm x 50mm. The back side of the card should be the logo on a black background. The front side should display the name 'Maple Ridge' along with standard information. The front's design should graphically complement the back.
Nice to have
• Any graphical elements in the front the complement the back side (with the logo on a black background) would be a plus.

```html
<!DOCTYPE html>
<html lang="en">
<head>
<meta charset="utf-8">
<title>Maple Ridge — Business Card</title>
<link href="https://fonts.googleapis.com/css2?family=Gentium+Book+Plus:wght@400;700&display=swap" rel="stylesheet">
<style>
  :root {
    --backdrop: #3a3a3c;
    --card-orange: #f28c1e;
    --card-black: #050505;
    --ink-white: #ffffff;
    --ink-black: #0a0a0a;
    --logo-orange: #f0a24a;
    --emblem-cream: #f3e2a4;
    --emblem-ring: #ef8a1c;
  }
  * { box-sizing: border-box; margin: 0; padding: 0; }
  html, body { width: 1200px; height: 926px; overflow: hidden; }
  body {
    background: var(--backdrop);
    font-family: "Gentium Book Plus", Georgia, serif;
    position: relative;
  }
  .card {
    position: absolute;
    top: 303px;
    width: 530px;
    height: 320px;
    overflow: hidden;
    box-shadow: 0 10px 30px rgba(0,0,0,.35);
  }
  .card-front { left: 50px; background: var(--card-orange); }
  .card-back  { left: 620px; background: var(--card-black); }

  .edge-bar {
    position: absolute;
    width: 6px;
    background: var(--ink-black);
  }
  .edge-bar.left  { left: 0; top: 120px; height: 90px; }
  .edge-bar.right { right: 0; top: 200px; height: 80px; }

  .holder-name {
    position: absolute;
    left: 50px; top: 34px;
    color: var(--ink-white);
    font-size: 36px;
    font-weight: 400;
    letter-spacing: .5px;
  }
  .holder-name strong { font-weight: 700; }

  .contact-list {
    position: absolute;
    left: 40px; top: 132px;
    width: 240px;
    list-style: none;
    color: var(--ink-white);
    font-size: 17px;
    line-height: 24px;
  }
  .contact-list li { display: flex; align-items: flex-start; gap: 8px; }
  .contact-icon {
    flex: none;
    width: 20px; height: 20px;
    margin-top: 2px;
    border-radius: 50%;
    background: var(--ink-black);
    display: flex; align-items: center; justify-content: center;
  }
  .contact-icon svg { width: 12px; height: 12px; }

  .brand-front {
    position: absolute;
    right: 30px; bottom: 30px;
    width: 190px;
    text-align: center;
  }
  .brand-front .emblem {
    width: 118px; height: 118px;
    margin: 0 auto 10px;
    border-radius: 50%;
    background: var(--emblem-cream);
    border: 4px solid var(--ink-white);
  }
  .brand-front .brand-name {
    color: var(--ink-white);
    font-size: 28px;
    font-weight: 700;
    letter-spacing: 1px;
    white-space: nowrap;
  }

  .brand-back {
    position: absolute;
    left: 0; right: 0; top: 48px;
    text-align: center;
  }
  .brand-back .emblem {
    width: 170px; height: 170px;
    margin: 0 auto 12px;
    border-radius: 50%;
    background: radial-gradient(circle at 55% 40%, #f6e8a8, #eeb45e 75%);
    border: 6px solid var(--emblem-ring);
  }
  .brand-back .brand-name {
    color: var(--logo-orange);
    font-size: 40px;
    font-weight: 700;
    letter-spacing: 1.5px;
  }
</style>
</head>
<body>

<section class="card card-front" aria-label="Card front">
  <span class="edge-bar left"></span>
  <span class="edge-bar right"></span>

  <h1 class="holder-name">Ethan <strong>Walker</strong></h1>

  <ul class="contact-list">
    <li>
      <span class="contact-icon"><svg viewBox="0 0 12 12"><path d="M2.5 1.5l2 .5.6 2.2-1.2.9a6 6 0 0 0 3 3l.9-1.2 2.2.6.5 2-1.2 1C5 10 2 7 1.5 2.7z" fill="#fff"/></svg></span>
      <span>555-274-1938</span>
    </li>
    <li>
      <span class="contact-icon"><svg viewBox="0 0 12 12"><rect x="1.5" y="3" width="9" height="6" fill="none" stroke="#fff" stroke-width="1.2"/><path d="M1.5 3l4.5 3.5L10.5 3" fill="none" stroke="#fff" stroke-width="1.2"/></svg></span>
      <span>mapleridge.co</span>
    </li>
    <li>
      <span class="contact-icon"><svg viewBox="0 0 12 12"><path d="M5 7l2-2M4.5 5.5L3 7a1.5 1.5 0 0 0 2 2l1.5-1.5M7.5 6.5L9 5a1.5 1.5 0 0 0-2-2L5.5 4.5" fill="none" stroke="#fff" stroke-width="1.2" stroke-linecap="round"/></svg></span>
      <span>ethan@mapleridge.co</span>
    </li>
    <li>
      <span class="contact-icon"><svg viewBox="0 0 12 12"><path d="M6 1.8L1.5 6h1.3v4h2.5V7.5h1.4V10h2.5V6h1.3z" fill="#fff"/></svg></span>
      <span>48 Harbor Lane, Suite 210,<br>Portland, OR 97204</span>
    </li>
  </ul>

  <div class="brand-front">
    <div class="emblem" role="img" aria-label="Brand emblem area"></div>
    <div class="brand-name">Maple Ridge</div>
  </div>
</section>

<section class="card card-back" aria-label="Card back">
  <div class="brand-back">
    <div class="emblem" role="img" aria-label="Brand emblem area with warm sunset tones"></div>
    <div class="brand-name">Maple Ridge</div>
  </div>
</section>

</body>
</html>
```